ESTIV Convention 2025 Quebec City

We would like to have a poster for the promotion and publicity of a convention for ESTIV. The goal is to obtain in A4 format and in US letter format (8.5 X 11) a poster for the upcoming convention in Quebec City.
Here are the 2 images (Maren-8 and Maren-24) that we chose yesterday and that inspire us.

Also the 3 posters of previous Conventions (Revue L+E 252, 261 & 273) As a model of what we are looking for.

As for what should also appear on the poster of the Quebec Convention 2025, here are the main points:

Mandatory at the very top of the poster: ESTIV and the wings (as on the posters of the previous Conventions attached) or at least leave such a space free because I believe that the printers of the High Chapter are redoing this acronym by themselves- same for the review Lys-Étoile.
Then the rest can be left to the imagination of the artists.

Here are the important things that should be included:
Harbor Accord
Quebec city
October 11 and 12, 2025
Light (This is the theme of the convention)
Glow to warm every heart (That's the name of the convention)

Please post it in French and NO RELATION TO RELIGIOUS OR RELIGION!!! :)

The website of the organization for more info if required is: www.lys-etoile-demo.org

If you think of anything else to add, no problem.

Target Market(s)

ESTIV members only

Industry/Entity Type

OSBL - Organisme philosophique ( non religieux )

Font styles to use
Serif
Sans Serif

Requirements
Must have
• ESTIV wings logo
Nice to have
• All in French and without reference to religion, also the GOLD color is appreciated
Should not have
• Of aspect or reference to the religious

```html
<!DOCTYPE html>
<html lang="fr">
<head>
<meta charset="utf-8">
<title>ESTIV — Accord du Port 2025</title>
<link href="https://fonts.googleapis.com/css2?family=Federo&family=Germania+One&display=swap" rel="stylesheet">
<style>
  :root {
    --sky-top: #0016d6;
    --sky-mid: #0a22f0;
    --sky-low: #1c50fb;
    --sky-bottom: #2466ff;
    --ink: #ffffff;
    --glow-core: #ffffff;
    --glow-rose: rgba(236, 180, 245, 0.75);
    --glow-halo: rgba(120, 150, 255, 0.45);
  }
  html, body {
    margin: 0;
    padding: 0;
    overflow: hidden;
  }
  .poster {
    position: relative;
    width: 851px;
    height: 1200px;
    overflow: hidden;
    background: linear-gradient(180deg, var(--sky-top) 0%, var(--sky-mid) 40%, var(--sky-low) 78%, var(--sky-bottom) 100%);
    color: var(--ink);
    font-family: "Federo", sans-serif;
    text-align: center;
  }
  .brand {
    position: absolute;
    top: 62px;
    left: 0;
    right: 0;
    display: flex;
    justify-content: center;
    align-items: center;
    gap: 14px;
    font-family: "Federo", sans-serif;
    font-size: 34px;
    letter-spacing: 0.32em;
    color: var(--ink);
  }
  .brand-dot {
    width: 14px;
    height: 14px;
    border-radius: 50%;
    background: var(--ink);
  }
  .title {
    position: absolute;
    top: 212px;
    left: 0;
    right: 0;
    margin: 0;
    font-family: "Germania One", sans-serif;
    font-weight: 400;
    font-size: 50px;
    line-height: 1;
    white-space: nowrap;
  }
  .subtitle {
    position: absolute;
    top: 288px;
    left: 0;
    right: 0;
    margin: 0;
    font-size: 38px;
    line-height: 1.1;
    letter-spacing: 0.08em;
  }
  .light-emblem {
    position: absolute;
    left: 192px;
    top: 448px;
    width: 470px;
    height: 470px;
    border-radius: 50%;
    background: radial-gradient(circle at 50% 50%,
      var(--glow-core) 0%,
      var(--glow-core) 8%,
      var(--glow-rose) 20%,
      var(--glow-halo) 45%,
      rgba(90, 120, 255, 0.18) 62%,
      rgba(60, 90, 255, 0) 72%);
  }
  .place {
    position: absolute;
    top: 1028px;
    left: 0;
    right: 0;
    margin: 0;
    font-size: 46px;
    line-height: 1.1;
    letter-spacing: 0.06em;
  }
  .date {
    position: absolute;
    top: 1098px;
    left: 0;
    right: 0;
    margin: 0;
    font-size: 40px;
    line-height: 1.1;
    letter-spacing: 0.08em;
  }
</style>
</head>
<body>
  <main class="poster">
    <div class="brand"><span class="brand-name">ESTIV</span><span class="brand-dot"></span></div>
    <h1 class="title">Rayonne Pour Réchauffer Chaque Cœur</h1>
    <p class="subtitle">Accord du Port</p>
    <div class="light-emblem" role="img" aria-label="Rayonnement lumineux central, étoile de lumière blanche et rosée sur fond bleu"></div>
    <p class="place">La ville de Québec</p>
    <p class="date">11 et 12 Octobre 2025</p>
  </main>
</body>
</html>
```